Sydney law firm, Prestwicks Solicitors, needs a flyer design!

We need a flyer design for our law firm which has been operating in Sydney for over 35 years. We want to send the flyer out to potential clients and also to existing clients to let them know the range of services that we provide. Our corporate colours are white, red and black and we would like these incorporated somewhat. The final design should be clean, modern and professional.

We would like the design to fit a double sided flyer approx. 210mm high x 100mm wide.

Industry/Entity Type

Law Firm

Font styles to use
Serif
Sans Serif

Colors
eb2026
ffffff

Requirements
Must have
• Details needed on the flyer are:
• Prestwicks Solicitors
• 3/82 Carradine Street, Liverpool, NSW 2170
• (02) 9418 3562
• www.prestwickssolicitors-example.com.au
• info@prestwickssolicitors-example.com.au
• Our areas of practice include:
• Property Law
• Conveyancing
• Leases
• Criminal Law
• Family Law
• Litigation and Dispute Resolution
• Company Law
• Wills and Estates
• Powers of Attorney and Guardianship
Should not have
• a picture of scales or a picture of a gavel

```html
<!DOCTYPE html>
<html lang="en">
<head>
<meta charset="utf-8">
<title>Prestwicks Solicitors – Flyer</title>
<link rel="stylesheet" href="https://fonts.googleapis.com/css2?family=Fira+Sans:wght@400;600&display=swap">
<style>
  :root {
    --brand-red: #eb2026;
    --brand-red-deep: #c8151b;
    --ink: #2a2a2a;
    --ink-soft: #555555;
    --paper: #ffffff;
    --backdrop: #e6e6e4;
    --stone-light: #d9d6d0;
    --stone-dark: #8f8b84;
  }
  * { box-sizing: border-box; margin: 0; padding: 0; }
  html, body {
    width: 1200px;
    height: 800px;
    overflow: hidden;
    background: var(--backdrop);
    font-family: "Fira Sans", Arial, sans-serif;
  }
  .flyer {
    position: absolute;
    left: 290px;
    top: 40px;
    width: 620px;
    height: 720px;
    background: var(--paper);
    box-shadow: 0 4px 18px rgba(0,0,0,0.18);
    overflow: hidden;
  }
  .flyer__hero {
    position: absolute;
    left: 0; top: 0;
    width: 100%;
    height: 330px;
    background: linear-gradient(160deg, var(--stone-light) 0%, #bdb9b2 55%, var(--stone-dark) 100%);
  }
  .flyer__intro {
    position: absolute;
    left: 40px;
    top: 362px;
    width: 290px;
    font-size: 13.5px;
    line-height: 1.32;
    color: var(--ink-soft);
  }
  .flyer__intro p + p { margin-top: 14px; }
  .brand {
    position: absolute;
    left: 40px;
    top: 548px;
    display: flex;
    align-items: center;
    gap: 10px;
  }
  .brand__mark {
    width: 14px; height: 14px;
    background: var(--brand-red);
  }
  .brand__name {
    font-size: 22px;
    font-weight: 600;
    color: var(--ink);
    letter-spacing: 0.5px;
  }
  .contact {
    position: absolute;
    left: 40px;
    top: 592px;
    list-style: none;
    font-size: 11.5px;
    line-height: 1.45;
    color: var(--brand-red);
  }
  .contact__web {
    position: absolute;
    left: 40px;
    top: 662px;
    font-size: 12px;
    font-weight: 600;
    color: var(--brand-red);
  }
  .services {
    position: absolute;
    left: 360px;
    top: 290px;
    width: 232px;
    height: 400px;
    border-radius: 22px;
    background: linear-gradient(180deg, var(--brand-red) 0%, var(--brand-red-deep) 100%);
    list-style: none;
    display: flex;
    flex-direction: column;
    justify-content: center;
    align-items: center;
    text-align: center;
    color: var(--paper);
    font-size: 16px;
    line-height: 1.15;
    padding: 14px 16px;
  }
  .services__item + .services__item::before {
    content: "•";
    display: block;
    font-size: 9px;
    line-height: 1;
    margin: 4px 0;
    opacity: 0.9;
  }
</style>
</head>
<body>
  <article class="flyer">
    <div class="flyer__hero" role="img" aria-label="Photograph of a stone office wall with the firm's name mounted as lettering"></div>

    <section class="flyer__intro">
      <p>Prestwicks Solicitors is a private law firm based in Liverpool that has been servicing the Sydney area for over 30 years. With a dedicated, professional and friendly team we pride ourselves on delivering an exceptional legal service to our clients.</p>
      <p>Offering a complete legal service at affordable rates, our clients really do come first.</p>
    </section>

    <div class="brand">
      <span class="brand__mark"></span>
      <span class="brand__name">Prestwicks Solicitors</span>
    </div>

    <ul class="contact">
      <li>3/82 Carradine Street, Liverpool, NSW 2170</li>
      <li>(02) 9418 3562</li>
      <li>info@prestwickssolicitors-example.com.au</li>
    </ul>
    <p class="contact__web">www.prestwickssolicitors-example.com.au</p>

    <ul class="services">
      <li class="services__item">Property Law</li>
      <li class="services__item">Conveyancing</li>
      <li class="services__item">Leases</li>
      <li class="services__item">Criminal Law</li>
      <li class="services__item">Family Law</li>
      <li class="services__item">Litigation and<br>Dispute Resolution</li>
      <li class="services__item">Company Law</li>
      <li class="services__item">Wills and Estates</li>
      <li class="services__item">Powers of Attorney and<br>Guardianship</li>
    </ul>
  </article>
</body>
</html>
```